Corvane Link Marketing Website

Corvane Link is the brand for a series of nation-wide internet peering exchanges operated by the Tallowmere Network Society Inc. (TNSI), a not-for-profit association founded in 1995.

Our current website is built on Drupal, and we are looking to migrate to WordPress with a similarly clean and modern theme:

http://www.corvanelink.example/

Target Market(s)

Technical and professional staff from the telecommunications industry in Australia.

Industry/Entity Type

Telecom

Font styles to use
Sans Serif

Requirements
Must have
• Responsive layout for mobile viewers
• Compatible with WordPress 4.2.2 and PHP 5.5.
• Winning entry will provide a completed WordPress theme file compatible .
• Usage of the "Corvane Link" logo must comply with the attached style guide.

```html
<!DOCTYPE html>
<html lang="en">
<head>
<meta charset="utf-8">
<title>Corvane Link — Internet Peering for Australia</title>
<link href="https://fonts.googleapis.com/css2?family=Open+Sans:ital,wght@0,400;0,600;0,700;1,400&family=Raleway:wght@400;500;600&display=swap" rel="stylesheet">
<style>
:root{
  --brand-blue:#3a63b8;
  --brand-navy:#1b3a86;
  --band-blue:#4a6fbf;
  --gold-top:#eec53c;
  --gold-bottom:#d9a11a;
  --ink:#222;
  --muted:#666;
  --soft:#f5f5f5;
  --white:#fff;
  --tick:#3a63b8;
}
*{box-sizing:border-box;margin:0;padding:0}
html,body{width:1200px;height:2378px;overflow:hidden}
body{position:relative;background:var(--white);font-family:"Open Sans",sans-serif;color:var(--ink)}
.abs{position:absolute}
.heading{font-family:"Raleway",sans-serif;font-weight:400}

/* header */
.site-header{left:0;top:0;width:1200px;height:90px;background:var(--white)}
.brand{left:214px;top:22px;display:flex;align-items:center;gap:10px}
.brand-mark{width:30px;height:30px;background:var(--brand-blue);border-radius:50%}
.brand-name{font-family:"Raleway",sans-serif;font-weight:600;font-size:26px;color:var(--brand-blue);letter-spacing:1px;line-height:1}
.brand-tag{left:256px;top:56px;font-family:"Raleway",sans-serif;font-size:9px;letter-spacing:1.6px;color:var(--brand-blue)}
.main-nav{left:591px;top:40px;display:flex;gap:33px;font-family:"Raleway",sans-serif;font-weight:500;font-size:13px;color:#333}

/* hero */
.hero{left:0;top:90px;width:1200px;height:471px;background:linear-gradient(160deg,#c9cfd6 0%,#5a6f8a 35%,#1f3050 65%,#0d1526 100%)}
.hero-title{left:0;top:262px;width:1200px;text-align:center;font-family:"Raleway",sans-serif;font-size:32px;color:var(--white)}
.hero-text{left:340px;top:308px;width:520px;text-align:center;font-family:"Raleway",sans-serif;font-size:13.5px;line-height:20px;color:var(--white)}
.hero-dots{left:566px;top:537px;display:flex;gap:4px}
.hero-dots span{width:13px;height:13px;border-radius:50%;background:var(--white)}

/* what we do */
.about-title{left:0;top:614px;width:1200px;text-align:center;font-size:30px;color:#111}
.about-text{left:230px;top:668px;width:740px;text-align:center;font-size:8.5px;line-height:13px;color:var(--muted)}
.about-text p+p{margin-top:8px}

/* values band */
.values{left:0;top:812px;width:1200px;height:353px;background:linear-gradient(180deg,#5678c4,#3f65b6)}
.value{width:260px;text-align:center;color:var(--white)}
.value svg{display:block;margin:0 auto}
.value h3{margin-top:14px;font-family:"Raleway",sans-serif;font-weight:500;font-size:15px;letter-spacing:.3px}
.value p{margin:6px auto 0;width:226px;font-size:10px;line-height:16.5px}

/* services */
.services-title{left:216px;top:1226px;font-size:30px;color:#111}
.services-text{left:216px;top:1274px;width:375px;font-size:9.5px;line-height:13px;color:var(--muted)}
.services-text p+p{margin-top:5px}
.services-list{left:216px;top:1372px;list-style:none;font-family:"Raleway",sans-serif;font-weight:500;font-size:12px;color:#222}
.services-list li{display:flex;align-items:center;gap:8px;height:24px}
.services-visual{left:610px;top:1276px;width:404px;height:174px;border-radius:8px;background:radial-gradient(ellipse at center,#dfe5ee 0%,#f4f6f9 70%,#fff 100%)}

/* testimonial */
.testimonial{left:0;top:1564px;width:1200px;height:287px;background:linear-gradient(180deg,var(--gold-top),var(--gold-bottom))}
.testimonial-title{left:0;top:1620px;width:1200px;text-align:center;font-size:27px;color:var(--white)}
.quote{left:277px;top:1664px;width:646px;text-align:center;font-style:italic;font-size:12.5px;line-height:23px;color:var(--white)}
.quote-mark{font-family:Georgia,serif;font-style:normal;font-size:34px;color:var(--white);line-height:1}
.quote-open{left:252px;top:1650px}
.quote-close{left:752px;top:1735px}
.client-name{left:0;top:1768px;width:1200px;text-align:center;font-weight:700;font-size:12.5px;color:var(--white)}
.client-role{left:0;top:1790px;width:1200px;text-align:center;font-size:9.5px;color:var(--white)}

/* partners */
.partners{left:0;top:1851px;width:1200px;height:257px;background:var(--soft)}
.partners-title{left:0;top:1902px;width:1200px;text-align:center;font-size:28px;color:#555}
.partner{top:1986px;font-family:"Raleway",sans-serif;font-weight:600;font-size:20px;color:#333;transform:translateX(-50%);white-space:nowrap}

/* footer */
.site-footer{left:0;top:2108px;width:1200px;height:270px;background:linear-gradient(180deg,#2d5aa8,#16307c)}
.footer-col{top:2148px;color:var(--white)}
.footer-col h4{font-family:"Raleway",sans-serif;font-weight:400;font-size:17px;margin-bottom:10px}
.footer-col li{list-style:none;font-size:10.5px;line-height:22px}
.copyright{left:230px;top:2341px;font-size:9px;color:#c8d3ea}
.social{left:890px;top:2339px;display:flex;gap:12px}
.social span{width:16px;height:16px;border-radius:50%;background:var(--white)}
</style>
</head>
<body>

<header class="site-header abs">
  <div class="brand abs" style="left:214px">
    <span class="brand-mark"></span>
    <span class="brand-name">CORVANE LINK</span>
  </div>
  <div class="brand-tag abs">INTERNET PEERING FOR AUSTRALIA</div>
  <nav class="main-nav abs">
    <span>HOME</span><span>ABOUT US</span><span>SERVICES</span><span>BLOG</span><span>CONTACT</span>
  </nav>
</header>

<section class="hero abs" role="img" aria-label="Close-up photograph of a network patch panel with blue cables"></section>
<h1 class="hero-title abs heading">Nation-wide Internet Peering</h1>
<p class="hero-text abs">In massa libero interdum nec interdum vel blandit sed nulla In ullamcorper est eget tempor cursus neque mi consectetuer mi a ultricies massa est sed nisl Class aptent taciti sociosqu ad litora torquent</p>
<div class="hero-dots abs"><span></span><span></span><span></span><span></span></div>

<h2 class="about-title abs heading">WHAT WE DO</h2>
<div class="about-text abs">
  <p>Aligula augue bibendum accumsan vestibulum ut commodo a mi Morbi ornare gravida elit integer congue augue et malesuada iaculis ipsum dui aliquet felis at cursus magna nisl nec elit Praesent elementum elit at tellus nec ultricies sit amet porttitor mattis enim in massa libero interdum nec interdum vel blandit sed nulla in ullamcorper est eget tempor</p>
  <p>Integer congue augue et malesuada iaculis ipsum dui aliquet felis at cursus magna nisl nec elit Praesent elementum elit at tellus nec ultricies sit amet porttitor mattis enim in massa libero interdum nec interdum vel blandit sed nulla In ullamcorper est eget tempor cursus neque mi consectetuer mi a ultricies massa est sed nisl Class aptent taciti sociosqu ad litora torquent per conubia nostra per inceptos hymenaeos Proin nulla arcu nonummy luctus dictum eget fermentum et lorem</p>
</div>

<section class="values abs" role="img" aria-label="Blue-tinted photograph of bundled network cables"></section>
<div class="value abs" style="left:203px;top:885px">
  <svg width="96" height="104" viewBox="0 0 96 104"><polygon points="48,3 92,28 92,76 48,101 4,76 4,28" fill="none" stroke="#fff" stroke-width="3"/><circle cx="48" cy="44" r="7" fill="#fff"/><circle cx="35" cy="48" r="5" fill="#fff"/><circle cx="61" cy="48" r="5" fill="#fff"/><path d="M36 66a12 11 0 0 1 24 0z" fill="#fff"/><path d="M26 64a9 8 0 0 1 12-7M70 64a9 8 0 0 0-12-7" stroke="#fff" stroke-width="4" fill="none"/></svg>
  <h3>MEMBER OWNED</h3>
  <p>Corvane Link is owned and operated by the Tallowmere Network Society Inc., meaning we are owned and run by our members. To get involved please email secretary@tnsi.example</p>
</div>
<div class="value abs" style="left:464px;top:885px">
  <svg width="96" height="104" viewBox="0 0 96 104"><polygon points="48,3 92,28 92,76 48,101 4,76 4,28" fill="none" stroke="#fff" stroke-width="3"/><rect x="30" y="40" width="36" height="26" rx="3" fill="#fff"/><rect x="41" y="34" width="14" height="8" rx="2" fill="none" stroke="#fff" stroke-width="3"/><rect x="45" y="50" width="6" height="5" fill="#4a6fbf"/></svg>
  <h3>COMMERCIALLY NEUTRAL</h3>
  <p>Corvane Link is owned and operated by the Tallowmere Network Society Inc., meaning we are owned and run by our members. To get involved please email secretary@tnsi.example</p>
</div>
<div class="value abs" style="left:727px;top:885px">
  <svg width="96" height="104" viewBox="0 0 96 104"><polygon points="48,3 92,28 92,76 48,101 4,76 4,28" fill="none" stroke="#fff" stroke-width="3"/><path d="M48 70C40 60 36 53 36 46a12 12 0 0 1 24 0c0 7-4 14-12 24z" fill="#fff"/><circle cx="48" cy="46" r="4.5" fill="#4a6fbf"/></svg>
  <h3>AUSTRALIA WIDE</h3>
  <p>Corvane Link is owned and operated by the Tallowmere Network Society Inc., meaning we are owned and run by our members. To get involved please email secretary@tnsi.example</p>
</div>

<h2 class="services-title abs heading">Services we Provide</h2>
<div class="services-text abs">
  <p>Aligula augue bibendum accumsan vestibulum ut commodo a mi Morbi ornare gravida elit Integer congue augue et malesuada</p>
  <p>felis at cursus magna nisl nec elit Praesent elementum elit at tellus nec ultricies sit amet porttitor mattis enim in massa libero interdum nec interdum vel blandit sed nulla In ullamcorper est eget temporconsectetuer mi a ultricies massa est sed</p>
</div>
<ul class="services-list abs">
  <li><svg width="13" height="13" viewBox="0 0 13 13"><circle cx="6.5" cy="6.5" r="6.5" fill="var(--tick)"/><path d="M3.5 6.8l2 2 4-4.2" stroke="#fff" stroke-width="1.6" fill="none"/></svg>PEERING POINTS ACROSS THE NATION</li>
  <li><svg width="13" height="13" viewBox="0 0 13 13"><circle cx="6.5" cy="6.5" r="6.5" fill="var(--tick)"/><path d="M3.5 6.8l2 2 4-4.2" stroke="#fff" stroke-width="1.6" fill="none"/></svg>MULTILATERAL PEERING POINTS</li>
  <li><svg width="13" height="13" viewBox="0 0 13 13"><circle cx="6.5" cy="6.5" r="6.5" fill="var(--tick)"/><path d="M3.5 6.8l2 2 4-4.2" stroke="#fff" stroke-width="1.6" fill="none"/></svg>MEMBER OWNED &amp; DRIVEN</li>
  <li><svg width="13" height="13" viewBox="0 0 13 13"><circle cx="6.5" cy="6.5" r="6.5" fill="var(--tick)"/><path d="M3.5 6.8l2 2 4-4.2" stroke="#fff" stroke-width="1.6" fill="none"/></svg>NOT-FOR-PROFIT</li>
  <li><svg width="13" height="13" viewBox="0 0 13 13"><circle cx="6.5" cy="6.5" r="6.5" fill="var(--tick)"/><path d="M3.5 6.8l2 2 4-4.2" stroke="#fff" stroke-width="1.6" fill="none"/></svg>STRONG MEMBERSHIP BASE</li>
</ul>
<div class="services-visual abs" role="img" aria-label="Illustration of laptops connected in a ring network around a central hub"></div>

<section class="testimonial abs"></section>
<h2 class="testimonial-title abs heading">WHAT OUR CLIENT SAYS</h2>
<span class="quote-mark quote-open abs">&ldquo;</span>
<p class="quote abs">Vivamus porttitor purus nisi eleifend libero a tempus libero lectus feugiat felis Morbi diam mauris viverra in gravida eu mattis in ante Morbi eget arcu Morbi porta libero id ullamcorper nonummy nibh ligula pulvinar metus eget consectetuer augue nisi quis lacus Ut ac mi quis lacus mollis aliquam Curabitur iaculis tempus eros Curabitur vel mi sit amet magna malesuada in tristique eu imperdiet ac</p>
<span class="quote-mark quote-close abs">&rdquo;</span>
<p class="client-name abs">Dr Elias Marwood</p>
<p class="client-role abs">Practice Head, Keystep Advisory Group</p>

<section class="partners abs"></section>
<h2 class="partners-title abs heading">Peering Partners</h2>
<span class="partner abs" style="left:269px">Norrow</span>
<span class="partner abs" style="left:393px">Veltrane</span>
<span class="partner abs" style="left:532px">Quillbase</span>
<span class="partner abs" style="left:662px">Opalnet</span>
<span class="partner abs" style="left:789px">Brindlecloud</span>
<span class="partner abs" style="left:925px">Harrowpoint</span>

<footer class="site-footer abs"></footer>
<div class="footer-col abs" style="left:231px"><h4>Quick Links</h4><ul><li>About Us</li><li>Our Technology</li><li>Clients</li><li>Testimonials</li></ul></div>
<div class="footer-col abs" style="left:407px"><h4>Services</h4><ul><li>Cras a ante vitae enim</li><li>Eaculis aliquam Mauris</li><li>Nquam venenatis</li><li>Euismod sit</li></ul></div>
<div class="footer-col abs" style="left:594px"><h4>Support</h4><ul><li>Support</li><li>Term of Use</li><li>Privacy Policy</li><li>Contact</li></ul></div>
<div class="footer-col abs" style="left:759px"><h4>Contact Us</h4><ul><li>PO Box 4120, Harbourline Centre</li><li>Perth, WA 6000 AUSTRALIA</li><li>Phone: 1300 000 417</li><li>Email: peering@corvanelink.example</li></ul></div>
<p class="copyright abs">© 2015 Company Name &nbsp;All right reserved &nbsp;Term of Use</p>
<div class="social abs"><span></span><span></span><span></span></div>

</body>
</html>
```